Hadley & Partners, LLC Business Card 2016

We need a new business card design for a very important trade show coming up.

We are a compliance Consulting Firm. Our clients are stock brokerage firms and investment advisers.

I would like our logo on both sides of the card.

Info in the front of the card shold include:

Logo
First & Last Name
Title
Office #
Cell #
Email
Company Address (42 W. Calloway St., Suite 300 Pasadena, CA 91417

Back of the card should include the logo and url: www.hadleypartnersgroup.com

Target Market(s)

Stock Brokerage Firms and Investment Advisers

Industry/Entity Type

Financial Service

Contact Information for Business Card

Marcus J. Pellew
President
42 W. Calloway St., Suite 300
Pasadena, CA 91417
O 626.555.0147 ext. 204
C 818.555.0193
Email: marcus@hadleypartnersgroup.com
www.hadleypartnersgroup.com

Requirements
Nice to have
• The back of the card could be black with the logo with the white letters.
• I do want the front of the card to at least have the color logo with the black "Hadley & Partners Lettering.

```html
<!DOCTYPE html>
<html lang="en">
<head>
<meta charset="utf-8">
<title>Hadley &amp; Partners — Business Card</title>
<link rel="stylesheet" href="https://fonts.googleapis.com/css2?family=Montserrat:wght@300;400&display=swap">
<style>
  :root {
    --bg: #e9e7e4;
    --card-dark: #0d0d0d;
    --card-dark-edge: #1c1c1c;
    --card-light: #ffffff;
    --accent: #d2232a;
    --ink: #1a1a1a;
    --muted: #8a8a8a;
    --white: #ffffff;
    --shadow: rgba(0,0,0,.18);
  }
  * { box-sizing: border-box; margin: 0; padding: 0; }
  html, body { width: 1200px; height: 900px; overflow: hidden; }
  body {
    background: var(--bg);
    font-family: "Montserrat", sans-serif;
    position: relative;
  }
  .card {
    position: absolute;
    width: 560px;
    height: 320px;
    border-radius: 22px;
    box-shadow: 0 14px 30px var(--shadow);
    overflow: hidden;
  }

  /* Back of card */
  .card-back {
    left: 80px; top: 100px;
    background: linear-gradient(135deg, var(--card-dark-edge) 0%, var(--card-dark) 55%, #151515 100%);
  }
  .card-back .brand {
    position: absolute;
    left: 0; right: 0; top: 120px;
    display: flex; align-items: center; justify-content: center; gap: 14px;
  }
  .card-back .brand-name { color: var(--white); font-size: 30px; }
  .card-back .url {
    position: absolute; left: 0; right: 0; top: 196px;
    text-align: center; color: var(--white);
    font-size: 13px; font-weight: 400; letter-spacing: .3px;
  }
  .card-back .url .domain { color: var(--accent); }

  .brand-mark { width: 22px; height: 22px; background: var(--accent); flex: none; }
  .brand-name {
    font-weight: 400;
    letter-spacing: 1.5px;
    text-transform: uppercase;
    white-space: nowrap;
  }

  /* Front of card */
  .card-front {
    left: 560px; top: 480px;
    background: var(--card-light);
  }
  .card-front .brand {
    position: absolute; right: 34px; top: 32px;
    display: flex; align-items: center; gap: 10px;
  }
  .card-front .brand-mark { width: 18px; height: 18px; }
  .card-front .brand-name { color: var(--ink); font-size: 19px; }
  .card-front .person { position: absolute; left: 38px; top: 120px; }
  .person .name { color: var(--accent); font-size: 19px; font-weight: 400; }
  .person .title { color: var(--muted); font-size: 12px; margin-top: 4px; }

  .contact {
    position: absolute; left: 38px; bottom: 30px;
    color: var(--muted); font-size: 12px; font-weight: 400; line-height: 1.55;
    list-style: none;
  }
  .contact li { display: flex; align-items: center; gap: 8px; }
  .contact .address { padding-left: 0; }
  .contact .address + .address { margin-bottom: 2px; }
  .contact svg { width: 11px; height: 11px; flex: none; fill: var(--accent); }
  .contact .plain { padding-left: 19px; }
</style>
</head>
<body>

  <section class="card card-back" aria-label="Back of business card">
    <div class="brand">
      <span class="brand-mark"></span>
      <span class="brand-name">Hadley &amp; Partners</span>
    </div>
    <p class="url">www.<span class="domain">hadleypartnersgroup</span>.com</p>
  </section>

  <section class="card card-front" aria-label="Front of business card">
    <div class="brand">
      <span class="brand-mark"></span>
      <span class="brand-name">Hadley &amp; Partners</span>
    </div>

    <div class="person">
      <p class="name">Marcus J. Pellew</p>
      <p class="title">President</p>
    </div>

    <ul class="contact">
      <li class="address">42 W. Calloway St., Suite 300</li>
      <li class="address">Pasadena, CA 91417</li>
      <li>
        <svg viewBox="0 0 12 12" aria-hidden="true"><path d="M2.2 0.8l2 2-1 1.3c.7 1.6 2 2.9 3.6 3.6l1.3-1 2 2-1.2 1.9C5 10.4 1.6 7 .4 2z"/></svg>
        626.555.0147 ext. 204
      </li>
      <li>
        <svg viewBox="0 0 12 12" aria-hidden="true"><path d="M3 0h6v12H3zM4 1.5v8h4v-8z"/></svg>
        818.555.0193
      </li>
      <li>
        <svg viewBox="0 0 12 12" aria-hidden="true"><path d="M0 2h12v8H0zM1 3l5 3.5L11 3z"/></svg>
        marcus@hadleypartnersgroup.com
      </li>
    </ul>
  </section>

</body>
</html>
```